Hydraulics Company Business Card Design

Modern business card design for a hydraulics company.
Our company colours are - black, orange and white.
I would like the following contact details included-
Name
Position
Phone number
Email
Website
Street Address

I have attached our company logo.
I would like the back of the card white.

Thank you.

```html
<!DOCTYPE html>
<html lang="en">
<head>
<meta charset="utf-8">
<title>Riverbend Hydraulics – Business Card</title>
<link href="https://fonts.googleapis.com/css2?family=Montserrat:wght@700&family=Open+Sans:wght@400;600&display=swap" rel="stylesheet">
<style>
  :root {
    --backdrop: #333333;
    --card: #ffffff;
    --orange: #f9a42a;
    --ink: #6d6d6d;
    --rule: #9a9a9a;
  }
  * { margin: 0; padding: 0; box-sizing: border-box; }
  html, body { width: 1200px; height: 780px; overflow: hidden; }
  body {
    background: var(--backdrop);
    display: flex;
    align-items: center;
    justify-content: center;
    gap: 40px;
    font-family: "Open Sans", sans-serif;
  }
  .card {
    position: relative;
    width: 540px;
    height: 310px;
    background: var(--card);
    border-radius: 24px;
    box-shadow: 0 6px 18px rgba(0,0,0,0.35);
    overflow: hidden;
  }
  .wordmark {
    font-family: "Montserrat", sans-serif;
    font-weight: 700;
    color: var(--orange);
    line-height: 1;
    text-align: right;
  }
  .wordmark .name { display: block; font-size: 50px; letter-spacing: -0.5px; }
  .wordmark .trade { display: block; font-size: 27px; letter-spacing: 2px; margin-top: 4px; }

  /* logo side */
  .card-front .wordmark { position: absolute; right: 60px; top: 108px; }

  /* details side */
  .card-back .wordmark { position: absolute; left: 0; right: 0; top: 46px; text-align: center; }
  .card-back .wordmark .name { font-size: 44px; }
  .card-back .wordmark .trade { font-size: 23px; }

  .person {
    position: absolute;
    right: 300px;
    top: 178px;
    text-align: right;
  }
  .person-name {
    font-family: "Montserrat", sans-serif;
    font-weight: 700;
    font-size: 18px;
    color: var(--orange);
    letter-spacing: 0.5px;
  }
  .person-role { font-size: 15px; color: var(--ink); margin-top: 2px; }

  .divider {
    position: absolute;
    left: 256px;
    top: 160px;
    width: 1px;
    height: 78px;
    background: var(--rule);
  }
  .contacts {
    position: absolute;
    left: 274px;
    top: 160px;
    list-style: none;
  }
  .contacts li {
    display: flex;
    align-items: center;
    gap: 7px;
    font-size: 15px;
    color: var(--ink);
    line-height: 26px;
  }
  .contacts svg { width: 14px; height: 14px; flex: none; }
  .address {
    position: absolute;
    left: 0; right: 0;
    bottom: 28px;
    text-align: center;
    font-size: 16px;
    color: var(--ink);
    letter-spacing: 0.3px;
  }
</style>
</head>
<body>
  <section class="card card-front" aria-label="Card front">
    <div class="wordmark">
      <span class="name">Riverbend</span>
      <span class="trade">HYDRAULICS</span>
    </div>
  </section>

  <section class="card card-back" aria-label="Card back">
    <div class="wordmark">
      <span class="name">Riverbend</span>
      <span class="trade">HYDRAULICS</span>
    </div>

    <div class="person">
      <p class="person-name">DANIEL CARTER</p>
      <p class="person-role">Managing Director</p>
    </div>

    <div class="divider"></div>

    <ul class="contacts">
      <li>
        <svg viewBox="0 0 14 14" aria-hidden="true"><circle cx="7" cy="7" r="7" fill="#f9a42a"/><path d="M4.2 3.5c.5-.3 1-.2 1.2.3l.5 1.2c.1.3 0 .6-.3.8l-.4.3c.4.9 1 1.5 1.9 1.9l.3-.4c.2-.3.5-.4.8-.3l1.2.5c.5.2.6.7.3 1.2-.5.8-1.4 1.1-2.3.7C5.8 9.1 4.9 8.2 4.3 6.6c-.4-1-.1-2.5-.1-3.1z" fill="#fff"/></svg>
        044-123 456 789
      </li>
      <li>
        <svg viewBox="0 0 14 14" aria-hidden="true"><circle cx="7" cy="7" r="7" fill="#f9a42a"/><rect x="3.5" y="4.5" width="7" height="5" fill="none" stroke="#fff" stroke-width="1"/><path d="M3.5 4.5 7 7.5l3.5-3" fill="none" stroke="#fff" stroke-width="1"/></svg>
        info@webname.com
      </li>
      <li>
        <svg viewBox="0 0 14 14" aria-hidden="true"><circle cx="7" cy="7" r="7" fill="#f9a42a"/><circle cx="7" cy="7" r="3.6" fill="none" stroke="#fff" stroke-width="1"/><path d="M3.4 7h7.2M7 3.4c-1.4 1.8-1.4 5.4 0 7.2M7 3.4c1.4 1.8 1.4 5.4 0 7.2" fill="none" stroke="#fff" stroke-width="0.8"/></svg>
        www.websitename.com
      </li>
    </ul>

    <p class="address">Your Address, City, State, Zip 0000</p>
  </section>
</body>
</html>
```